Park Company Mobile Application Design

We are looking for deisgn of the mobile application for the parking company. More details about the parking company you can find on the following web site: www.lumrapark.mk.
As well we attached the parking card that this company is issuing. As you may see their preferred color is green.
Attached you can find screens that we are planning to implement in the mobile application.
If you need more details please contact us on dragan@kestrel.mk.

Thanks,
Dragan Petrusev
Kestrel Group

```html
<!DOCTYPE html>
<html lang="ru">
<head>
<meta charset="utf-8">
<title>ЛУМРА — мобильное приложение парковки</title>
<link href="https://fonts.googleapis.com/css2?family=Noto+Sans:wght@400;500;700&display=swap" rel="stylesheet">
<style>
  :root {
    --canvas: #d2d2d2;
    --phone: #242840;
    --field: #363a4f;
    --field-line: #2c3048;
    --nav: #353950;
    --green: #4fb947;
    --green-dark: #2f7d2c;
    --text: #e9eaf0;
    --muted: #b7bac8;
    --map: #5e7462;
  }
  * { box-sizing: border-box; margin: 0; padding: 0; }
  html, body { width: 706px; height: 1200px; overflow: hidden; background: var(--canvas); }
  body { position: relative; font-family: "Noto Sans", Arial, sans-serif; color: var(--text); }

  .phone {
    position: absolute; width: 290px; height: 627px;
    background: var(--phone); border-radius: 28px; overflow: hidden;
    transform: scale(0.4764); transform-origin: top left;
  }
  .abs { position: absolute; }
  .center { left: 0; right: 0; text-align: center; }

  .brand { display: flex; align-items: center; justify-content: center; gap: 8px;
    color: var(--green); font-weight: 700; letter-spacing: 2px; }
  .brand .dot { width: 14px; height: 14px; border-radius: 50%; background: var(--green); }
  .brand.large { font-size: 30px; }
  .brand.large .dot { width: 22px; height: 22px; }
  .brand.small { font-size: 15px; }

  .fields { position: absolute; left: 13px; width: 263px; background: var(--field); border-radius: 6px; overflow: hidden; }
  .field { height: 41px; display: flex; align-items: center; padding: 0 13px;
    font-size: 11px; color: var(--muted); border-bottom: 1px solid var(--field-line); gap: 12px; }
  .field:last-child { border-bottom: none; }
  .field svg.ic { width: 16px; height: 16px; flex: none; }
  .field .eye { margin-left: auto; width: 14px; height: 10px; }

  .btn { position: absolute; left: 38px; width: 215px; height: 38px; border-radius: 3px;
    display: flex; align-items: center; justify-content: center; gap: 6px;
    font-size: 12px; font-weight: 700; letter-spacing: .3px; }
  .btn.solid { background: var(--green); color: #fff; }
  .btn.outline { border: 1.5px solid var(--green); color: var(--green); }

  .caption { font-size: 10.5px; font-weight: 500; }
  .link { font-size: 9px; text-decoration: underline; }
  .lead { font-size: 13px; line-height: 1.5; padding: 0 10px; }

  .topbar { position: absolute; top: 35px; left: 0; right: 0; height: 26px; }
  .menu { position: absolute; left: 15px; top: 6px; width: 14px; height: 12px; }
  .topbar .brand { position: absolute; left: 0; right: 0; top: 2px; }

  .nav { position: absolute; left: 0; right: 0; bottom: 0; height: 70px; background: var(--nav);
    display: flex; }
  .nav .tab { flex: 1; display: flex; flex-direction: column; align-items: center; justify-content: center; gap: 4px;
    font-size: 9px; font-weight: 700; white-space: nowrap; }
  .nav svg { width: 26px; height: 22px; }

  .map { position: absolute; inset: 0 0 70px 0;
    background: linear-gradient(160deg, #6b806d 0%, var(--map) 55%, #536857 100%); }
  .pin { position: absolute; width: 40px; height: 58px; }

  .photo-top { position: absolute; left: 0; top: 0; width: 290px; height: 291px;
    background: radial-gradient(ellipse at 50% 45%, #94a79a 0%, #889b8f 50%, #6f8276 100%); }
  .handle { position: absolute; top: 303px; left: 126px; width: 38px; height: 3px; background: #fff; border-radius: 2px; }

  .card-art { position: absolute; left: 13px; top: 85px; width: 263px; height: 135px; border-radius: 8px;
    background: linear-gradient(180deg, #3fa845 0%, #1f7a2c 55%, #0f4f1e 100%);
    box-shadow: 0 3px 8px rgba(0,0,0,.35); }
  .card-name { position: absolute; left: 56px; top: 18px; font-size: 30px; font-weight: 700; line-height: 1;
    color: #fff; }

  .info { position: absolute; left: 13px; width: 263px; background: var(--field); border-radius: 6px;
    font-size: 10.5px; font-weight: 500; }
  .info .row { display: flex; }
  .info .cell { flex: 1; display: flex; align-items: center; gap: 8px; padding-left: 13px; }
  .info svg { width: 16px; height: 14px; flex: none; }

  .textarea { position: absolute; left: 13px; top: 163px; width: 263px; height: 83px; background: var(--field);
    border-radius: 0 0 6px 6px; font-size: 11px; color: var(--muted); padding: 14px 11px; }
  .select { position: absolute; left: 13px; top: 122px; width: 263px; height: 41px; background: var(--field);
    border-radius: 6px 6px 0 0; border-bottom: 1px solid var(--field-line);
    display: flex; align-items: center; justify-content: space-between; padding: 0 11px; font-size: 11px; color: var(--muted); }
  .section-title { font-size: 17px; font-weight: 700; line-height: 1.35; }
  .report { position: absolute; left: 13px; width: 263px; height: 54px; background: var(--field); border-radius: 5px; overflow: hidden; }
  .report .thumb { position: absolute; left: 0; top: 0; width: 77px; height: 100%;
    background: linear-gradient(135deg, #7d8086 0%, #4a4d55 60%, #2d2f36 100%); }
  .report .title { position: absolute; left: 90px; top: 8px; font-size: 12px; font-weight: 700; }
  .report .desc { position: absolute; left: 88px; top: 32px; font-size: 11px; }
</style>
</head>
<body>

<svg width="0" height="0" style="position:absolute">
  <defs>
    <symbol id="i-mail" viewBox="0 0 16 16"><rect x="1" y="3" width="14" height="10" fill="none" stroke="#4fb947" stroke-width="1.3"/><path d="M1 3l7 6 7-6" fill="none" stroke="#4fb947" stroke-width="1.3"/></symbol>
    <symbol id="i-lock" viewBox="0 0 16 16"><rect x="2.5" y="7" width="11" height="8" rx="1" fill="none" stroke="#4fb947" stroke-width="1.3"/><path d="M5 7V5a3 3 0 016 0v2" fill="none" stroke="#4fb947" stroke-width="1.3"/><path d="M8 10v2" stroke="#4fb947" stroke-width="1.3"/></symbol>
    <symbol id="i-eye" viewBox="0 0 14 10"><path d="M1 2c3 4 9 4 12 0M4 5l-1 2M7 6v2M10 5l1 2" fill="none" stroke="#4fb947" stroke-width="1.2"/></symbol>
    <symbol id="i-phone" viewBox="0 0 16 16"><path d="M3 1.5l3 .5 1 3.5-2 1.5c1 2 2.5 3.5 4.5 4.5L11 9l3.5 1 .5 3c-1 1.5-2.5 2-4 1.5C6 13 3 10 1.5 5.5 1 4 1.5 2.5 3 1.5z" fill="none" stroke="#4fb947" stroke-width="1.2"/></symbol>
    <symbol id="i-pin" viewBox="0 0 16 16"><path d="M8 15s-5-5-5-8.5a5 5 0 0110 0C13 10 8 15 8 15z" fill="none" stroke="#4fb947" stroke-width="1.3"/><circle cx="8" cy="6.5" r="2" fill="none" stroke="#4fb947" stroke-width="1.2"/></symbol>
    <symbol id="i-clock" viewBox="0 0 16 16"><circle cx="8" cy="8" r="6.5" fill="none" stroke="#4fb947" stroke-width="1.3"/><path d="M8 4v4h3" fill="none" stroke="#4fb947" stroke-width="1.3"/></symbol>
    <symbol id="i-car" viewBox="0 0 16 14"><path d="M2 7l1.5-4h9L14 7M1 7h14v5H1zM3 12v1.5M13 12v1.5" fill="none" stroke="#4fb947" stroke-width="1.2"/><circle cx="4" cy="9.5" r="1" fill="#4fb947"/><circle cx="12" cy="9.5" r="1" fill="#4fb947"/></symbol>
    <symbol id="i-cal" viewBox="0 0 16 14"><rect x="1.5" y="2" width="13" height="11" fill="none" stroke="#4fb947" stroke-width="1.2"/><path d="M1.5 5.5h13M5 0.5v3M11 0.5v3" stroke="#4fb947" stroke-width="1.2"/></symbol>
    <symbol id="i-cam" viewBox="0 0 16 14"><rect x="1" y="3" width="14" height="10" rx="1" fill="none" stroke="#4fb947" stroke-width="1.3"/><path d="M5 3l1.5-2h3L11 3" fill="none" stroke="#4fb947" stroke-width="1.3"/><circle cx="8" cy="8" r="2.6" fill="none" stroke="#4fb947" stroke-width="1.3"/></symbol>
    <symbol id="i-menu" viewBox="0 0 14 12"><path d="M0 1h14M0 6h14M0 11h14" stroke="#fff" stroke-width="1.4"/></symbol>
    <symbol id="i-back" viewBox="0 0 14 12"><path d="M13 6H2M6 1L1 6l5 5" fill="none" stroke="#fff" stroke-width="1.5"/></symbol>
    <symbol id="n-car" viewBox="0 0 26 22"><path d="M3 15l2.5-5h13L21 15z" fill="#4fb947"/><rect x="1" y="15" width="22" height="4" rx="1.5" fill="#3c9d36"/><circle cx="6" cy="19.5" r="2" fill="#1e2235"/><circle cx="18" cy="19.5" r="2" fill="#1e2235"/><rect x="21" y="2" width="1.4" height="12" fill="#ddd"/><rect x="19" y="1" width="6" height="5" fill="#4fb947"/></symbol>
    <symbol id="n-cash" viewBox="0 0 26 22"><rect x="7" y="3" width="14" height="8" rx="1" transform="rotate(-25 14 7)" fill="#4fb947"/><path d="M3 17c3-4 7-6 12-5l-3 3 5 1" fill="none" stroke="#f1e7d8" stroke-width="3" stroke-linecap="round"/></symbol>
    <symbol id="n-cone" viewBox="0 0 26 22"><path d="M13 1l6 18H7z" fill="#4fb947"/><path d="M10.4 9h5.2M9.3 13h7.4" stroke="#fff" stroke-width="1.8"/><rect x="5" y="19" width="16" height="2.5" fill="#3c9d36"/></symbol>
    <symbol id="map-pin" viewBox="0 0 40 58"><path d="M20 56C20 56 2 34 2 21a18 18 0 0136 0C38 34 20 56 20 56z" fill="#242840"/><text x="20" y="28" text-anchor="middle" font-size="18" fill="#4fb947" font-family="Noto Sans, sans-serif">P</text></symbol>
  </defs>
</svg>

<!-- Вход -->
<section class="phone" style="left:65px; top:49px;">
  <div class="brand large abs center" style="top:175px;"><span class="dot"></span>ЛУМРА</div>
  <div class="fields" style="top:293px;">
    <div class="field"><svg class="ic"><use href="#i-mail"/></svg>Отправить по электронной почте</div>
    <div class="field"><svg class="ic"><use href="#i-lock"/></svg>Пароль<svg class="eye"><use href="#i-eye"/></svg></div>
  </div>
  <div class="abs center link" style="top:396px;">Забыли пароль?</div>
  <div class="btn solid" style="top:427px;">Входа</div>
  <div class="abs center caption" style="top:527px;">У вас нет учетной записи?</div>
  <div class="btn outline" style="top:561px;">Регистрация</div>
</section>

<!-- Регистрация -->
<section class="phone" style="left:284px; top:49px;">
  <div class="brand large abs center" style="top:125px;"><span class="dot"></span>ЛУМРА</div>
  <div class="fields" style="top:241px;">
    <div class="field"><svg class="ic"><use href="#i-mail"/></svg>Отправить по электронной почте</div>
    <div class="field"><svg class="ic"><use href="#i-lock"/></svg>Пароль<svg class="eye"><use href="#i-eye"/></svg></div>
    <div class="field"><svg class="ic"><use href="#i-lock"/></svg>Подтверждение пароля<svg class="eye"><use href="#i-eye"/></svg></div>
    <div class="field"><svg class="ic"><use href="#i-phone"/></svg>Телефон</div>
  </div>
  <div class="btn solid" style="top:427px;">Регистрация</div>
  <div class="abs center caption" style="top:527px;">У вас уже есть учетная запись?</div>
  <div class="btn outline" style="top:561px;">Входа</div>
</section>

<!-- Забыли пароль -->
<section class="phone" style="left:503px; top:49px;">
  <svg class="abs" style="left:15px; top:39px; width:14px; height:12px;"><use href="#i-back"/></svg>
  <div class="abs" style="left:88px; top:35px; font-size:13.5px;">Забыли пароль</div>
  <div class="abs center lead" style="top:183px;">Пожалуйста, введите свою электронную почту, чтобы мы может отправить код для сброса ваш пароль</div>
  <div class="fields" style="top:261px;">
    <div class="field"><svg class="ic"><use href="#i-mail"/></svg>Отправить по электронной почте</div>
  </div>
  <div class="btn solid" style="top:329px;">Отправить код</div>
  <div class="abs center caption" style="top:527px;">Альтернативная кодовая система</div>
  <div class="btn outline" style="top:561px;">Отправить код по SMS</div>
</section>

<!-- Карта -->
<section class="phone" style="left:65px; top:433px;">
  <div class="map" role="img" aria-label="Карта города с улицами и кварталами"></div>
  <div class="topbar">
    <svg class="menu"><use href="#i-menu"/></svg>
    <div class="brand small"><span class="dot"></span>ЛУМРА</div>
  </div>
  <svg class="pin" style="left:86px; top:72px;"><use href="#map-pin"/></svg>
  <svg class="pin" style="left:138px; top:282px;"><use href="#map-pin"/></svg>
  <div class="abs" style="left:134px; top:332px; width:16px; height:16px; border-radius:50%; background:rgba(79,185,71,.35); border:2px solid var(--green);"></div>
  <svg class="pin" style="left:258px; top:517px;"><use href="#map-pin"/></svg>
  <div class="btn solid" style="top:491px;">Парк сейчас</div>
  <nav class="nav">
    <div class="tab"><svg><use href="#n-car"/></svg>Платная парковка</div>
    <div class="tab"><svg><use href="#n-cash"/></svg></div>
    <div class="tab"><svg><use href="#n-cone"/></svg></div>
  </nav>
</section>

<!-- Оплата парковки -->
<section class="phone" style="left:284px; top:433px;">
  <div class="photo-top" role="img" aria-label="Размытая фотография улицы с припаркованными машинами"></div>
  <div class="handle"></div>
  <div class="abs center lead" style="top:344px; font-size:12px; line-height:1.4;">Пожалуйста, заполните поля, чтобы припарковаться и оплатить</div>
  <div class="fields" style="top:397px;">
    <div class="field"><svg class="ic"><use href="#i-pin"/></svg>Расположение</div>
    <div class="field"><svg class="ic"><use href="#i-clock"/></svg>Время</div>
    <div class="field"><svg class="ic"><use href="#i-car"/></svg>Лицензионная табличка</div>
  </div>
  <div class="btn solid" style="top:561px;">Платная парковка</div>
</section>

<!-- Карта пользователя -->
<section class="phone" style="left:503px; top:433px;">
  <div class="topbar">
    <svg class="menu"><use href="#i-menu"/></svg>
    <div class="brand small"><span class="dot"></span>ЛУМРА</div>
  </div>
  <div class="card-art" role="img" aria-label="Зелёная парковочная карта с изображением здания">
    <div class="card-name">LeafPass<br>Card</div>
  </div>
  <div class="btn solid" style="top:247px;">Купить часы</div>
  <div class="btn outline" style="top:305px;">Объявить гостя</div>
  <div class="info" style="top:382px; height:53px;">
    <div class="row" style="height:53px;">
      <div class="cell"><svg><use href="#i-car"/></svg>CKC-234</div>
      <div class="cell"><svg><use href="#i-clock"/></svg>120 мин.</div>
    </div>
  </div>
  <div class="info" style="top:444px; height:97px;">
    <div class="row" style="height:38px; justify-content:center; align-items:center; gap:8px;"><svg><use href="#i-car"/></svg>CKC-234</div>
    <div class="row" style="height:28px;">
      <div class="cell"><svg><use href="#i-cal"/></svg>18/12/2019</div>
      <div class="cell"><svg><use href="#i-cal"/></svg>19/12/2019</div>
    </div>
    <div class="row" style="height:28px;">
      <div class="cell"><svg><use href="#i-clock"/></svg>18:00:00</div>
      <div class="cell"><svg><use href="#i-clock"/></svg>18:00:00</div>
    </div>
  </div>
  <nav class="nav">
    <div class="tab"><svg><use href="#n-car"/></svg></div>
    <div class="tab"><svg><use href="#n-cash"/></svg>Карта пользователя</div>
    <div class="tab"><svg><use href="#n-cone"/></svg></div>
  </nav>
</section>

<!-- Сообщить о проблеме -->
<section class="phone" style="left:284px; top:816px;">
  <div class="topbar">
    <svg class="menu"><use href="#i-menu"/></svg>
    <div class="brand small"><span class="dot"></span>ЛУМРА</div>
  </div>
  <div class="abs center" style="top:87px; font-size:12px;">Заполните детали, чтобы сообщить</div>
  <div class="select">Категории<svg width="8" height="5" viewBox="0 0 8 5"><path d="M1 1l3 3 3-3" fill="none" stroke="#4fb947" stroke-width="1.2"/></svg></div>
  <div class="textarea">Описание</div>
  <div class="btn outline" style="top:266px;"><svg width="16" height="14"><use href="#i-cam"/></svg>Захват или Галерея</div>
  <div class="btn solid" style="top:343px;">Отчет</div>
  <div class="abs center section-title" style="top:412px;">Недавний отчет, составленный<br>Вами</div>
  <div class="report" style="top:478px;">
    <div class="thumb" role="img" aria-label="Фото поцарапанного автомобиля"></div>
    <div class="title">Царапин</div>
    <div class="desc">Прошлой ночью моя машина</div>
  </div>
  <div class="report" style="top:540px;">
    <div class="thumb" role="img" aria-label="Фото автомобиля с вмятиной"></div>
    <div class="title" style="left:77px;">Вмятины</div>
  </div>
  <nav class="nav">
    <div class="tab"><svg><use href="#n-car"/></svg></div>
    <div class="tab"><svg><use href="#n-cash"/></svg></div>
    <div class="tab"><svg><use href="#n-cone"/></svg>Сообщить о проблеме</div>
  </nav>
</section>

</body>
</html>
```